Radiant Crossroads - An Exciting Mission & Book Cover Project

Help me to inspire people to live their best life! This is a mission, not just a design project.
I need a Book Cover designed to keep me inspired on the process of writing my book.
Book Title: Radiant Crossroads
Tag Line: Three Simple Steps to get out of your own way, SuperCharge your Life and Step into Purpose!
Author: Marlon Teague

The three steps are: Ownership, Vision and Action (Not sure if this should be on the front or back of the book cover)

The book is a self-help, motivational book. Personal development.
The cover needs to be strong and capture peoples attention, especially with competing shelf space. I almost see a fire ball of flame or explosion that will grab peoples attention.
My company is The Summit Collective. I have added the company logo and a few pages of my presentation and topic outline to give an idea.
Maybe: The Summit Collective logo on back of the cover. website is marlonteague-example.com

THOUGHT: People should be able to take a photo of them holding the book cover showing what area of life they want Radiant Crossroads in. This is why the front cover must be so visual and powerful that they want to take a photo with it. Ie. Explosion, fire, strong and bold.

Target Market(s)

Anyone who feels stuck and needs to breakthrough and move forward in life.

Industry/Entity Type

Motivation

Font styles to use
Serif
Sans Serif

Colors
ec1f27
f37122
fbed22

Requirements
Must have
• The design must be STRONG, SIMPLE, STAND OUT ON BOOK SHELVES.
Must have an open file to swap the photo and copy out.

Back Cover Page
1) Summary
2) 2-3 testimonials. One sentence.
3) About the Author (maybe with photo)
4) Summit Collective logo
5) Website: radiantcrossroads-example.com and marlonteague-example.com
Nice to have
• If my photo works somewhere that would be great. I will change the photo later.
Added Where Does Your Compass Point? a nice cover example.
Should not have
• Right now I am writing the summary for the back of the cover. For now use Loreum Ipsum text and 2-3 recommendations. Again, I will get these only later.

```html
<!DOCTYPE html>
<html lang="en">
<head>
<meta charset="utf-8">
<title>Radiant Crossroads – Book Cover</title>
<link rel="stylesheet" href="https://fonts.googleapis.com/css2?family=Oswald:wght@500;600&family=Roboto+Condensed:wght@700&display=swap">
<style>
  :root {
    --backdrop: #333333;
    --paper: #f2f2f2;
    --paper-shadow: #d9d9d9;
    --red: #d9121c;
    --ink: #2e2e2e;
    --flame-red: #ec1f27;
    --flame-orange: #f37122;
    --flame-yellow: #fbed22;
    --void: #0a0604;
  }
  * { margin: 0; padding: 0; box-sizing: border-box; }
  html, body {
    width: 1200px; height: 1200px; overflow: hidden;
    background: var(--backdrop);
  }
  .cover {
    position: absolute; left: 216px; top: 24px;
    width: 768px; height: 1152px;
    background: var(--paper);
    overflow: hidden;
  }
  .author {
    position: absolute; top: 48px; left: 0; width: 100%;
    text-align: center;
    font-family: "Roboto Condensed", "Arial Narrow", sans-serif;
    font-weight: 700; font-size: 62px; line-height: 1;
    letter-spacing: 7px;
    color: var(--red);
  }
  .burst-art {
    position: absolute; left: 0; top: 140px;
    width: 768px; height: 760px;
  }
  .title {
    position: absolute; top: 400px; left: 0; width: 100%;
    text-align: center;
    font-family: "Oswald", "Arial Narrow", sans-serif;
    font-weight: 500; font-size: 142px; line-height: 1.0;
    text-transform: uppercase;
    letter-spacing: -1px;
  }
  .title span {
    display: block;
    background: linear-gradient(90deg, var(--flame-red) 0%, var(--flame-orange) 30%, #f9b233 55%, var(--flame-orange) 78%, var(--flame-red) 100%);
    -webkit-background-clip: text; background-clip: text;
    color: transparent;
  }
  .tagline {
    position: absolute; top: 928px; left: 0; width: 100%;
    text-align: center;
    font-family: "Roboto Condensed", "Arial Narrow", sans-serif;
    font-weight: 700; font-size: 35px; line-height: 46px;
    text-transform: uppercase;
    color: var(--ink);
  }
  .tagline .accent { color: var(--red); }
</style>
</head>
<body>
  <main class="cover">
    <div class="author">Marlon Teague</div>

    <svg class="burst-art" viewBox="0 0 768 760" role="img" aria-label="Illustration of a white wall blasting apart with flames blazing through the hole">
      <defs>
        <radialGradient id="wallShade" cx="50%" cy="50%" r="60%">
          <stop offset="0%" stop-color="#e4e4e4"/>
          <stop offset="100%" stop-color="#f2f2f2"/>
        </radialGradient>
        <radialGradient id="fireHole" cx="50%" cy="52%" r="55%">
          <stop offset="0%" stop-color="#0a0604"/>
          <stop offset="55%" stop-color="#1a0b04"/>
          <stop offset="78%" stop-color="#b8400f"/>
          <stop offset="92%" stop-color="#f37122"/>
          <stop offset="100%" stop-color="#fbb034"/>
        </radialGradient>
      </defs>
      <rect width="768" height="760" fill="url(#wallShade)"/>
      <ellipse cx="384" cy="375" rx="375" ry="250" fill="#cfcfcf" opacity="0.5"/>
      <ellipse cx="384" cy="375" rx="360" ry="235" fill="url(#fireHole)"/>
    </svg>

    <h1 class="title"><span>Radiant</span><span>Crossroads</span></h1>

    <p class="tagline">
      <span class="accent">Three Simple Steps</span> to<br>
      Get out of your own way, Supercharge<br>
      <span class="accent">Your Life</span> and Step <span class="accent">into Purpose!</span>
    </p>
  </main>
</body>
</html>
```